Pull Up Banners

Would like to have these pull up banner designs changed to a new modern theme. I have running a sales booth and want to re-design the banner designs. I have uploaded old banner design, I need phone number and website added onto bottom. Happy to consider images to attract people attention to increase sales and spark people interest walking past.

```html
<!DOCTYPE html>
<html lang="en">
<head>
<meta charset="utf-8">
<title>BrightDesk Pull Up Banners</title>
<link rel="stylesheet" href="https://fonts.googleapis.com/css2?family=Montserrat:ital,wght@0,300;0,400;0,500;0,600;0,700;0,800;1,400;1,800&display=swap">
<style>
  :root {
    --orange: #f26522;
    --orange-deep: #d9481a;
    --orange-soft: #f9a475;
    --black: #141414;
    --charcoal: #2a2a2a;
    --white: #ffffff;
    --silver: #c9c9c9;
    --page: #e8e8e8;
  }
  html, body {
    margin: 0;
    padding: 0;
    width: 1107px;
    height: 1200px;
    overflow: hidden;
    background: var(--page);
    font-family: "Montserrat", Arial, sans-serif;
  }
  .canvas {
    position: relative;
    width: 1107px;
    height: 1200px;
  }
  .banner {
    position: absolute;
    top: 129px;
    width: 376px;
    height: 940px;
    box-shadow: 0 2px 6px rgba(0,0,0,0.12);
  }
  .banner--front { left: 172px; }
  .banner--back { left: 558px; }
  .banner svg { display: block; width: 376px; height: 940px; }
  .side-label {
    position: absolute;
    top: 1080px;
    margin: 0;
    font-weight: 700;
    font-size: 19px;
    letter-spacing: 1px;
    color: var(--orange);
  }
  .side-label--front { left: 172px; }
  .side-label--back { left: 558px; }

  .brand-name { font-weight: 700; font-size: 46px; fill: var(--orange); letter-spacing: 2px; }
  .headline { font-weight: 800; fill: var(--orange); text-anchor: middle; }
  .lead-light { font-weight: 300; fill: var(--orange); }
  .lead-bold { font-weight: 800; fill: var(--orange); }
  .lead-white { font-weight: 800; fill: var(--white); text-anchor: middle; font-size: 38px; }
  .pill-text { font-size: 36px; fill: var(--black); text-anchor: middle; }
  .pill-light { font-weight: 400; }
  .pill-bold { font-weight: 800; }
  .service-label { font-weight: 700; font-size: 16px; fill: var(--white); text-anchor: middle; }
  .cta-text { font-weight: 800; font-size: 30px; fill: var(--white); text-anchor: middle; letter-spacing: 1px; }
  .cta-sub { font-size: 20px; fill: var(--white); text-anchor: middle; font-style: italic; font-weight: 400; }
  .cta-sub-bold { font-weight: 800; }
  .web-caps { font-weight: 700; font-size: 16px; fill: var(--white); text-anchor: middle; letter-spacing: 0.5px; }
  .web-caps--orange { fill: var(--orange); font-size: 20px; }
  .contact-line { font-weight: 500; font-size: 13px; fill: var(--black); }
  .phone-number { font-weight: 500; font-size: 32px; fill: var(--black); }
</style>
</head>
<body>
<main class="canvas">

  <svg width="0" height="0" style="position:absolute" aria-hidden="true">
    <defs>
      <linearGradient id="panel-bg" x1="0" y1="0" x2="1" y2="0">
        <stop offset="0" stop-color="#d2d2d2"/>
        <stop offset="0.5" stop-color="#f7f7f7"/>
        <stop offset="1" stop-color="#d2d2d2"/>
      </linearGradient>
      <linearGradient id="silver-pill" x1="0" y1="0" x2="1" y2="1">
        <stop offset="0" stop-color="#9a9a9a"/>
        <stop offset="0.45" stop-color="#f4f4f4"/>
        <stop offset="1" stop-color="#a8a8a8"/>
      </linearGradient>
      <linearGradient id="dark-section" x1="0" y1="0" x2="0" y2="1">
        <stop offset="0" stop-color="#0d0d0d"/>
        <stop offset="0.5" stop-color="#262626"/>
        <stop offset="1" stop-color="#111111"/>
      </linearGradient>
      <linearGradient id="photo-tones" x1="0" y1="0" x2="1" y2="1">
        <stop offset="0" stop-color="#dfe3ea"/>
        <stop offset="0.55" stop-color="#e8cdbd"/>
        <stop offset="1" stop-color="#f3f1ef"/>
      </linearGradient>
      <linearGradient id="sketch-tones" x1="0" y1="0" x2="1" y2="1">
        <stop offset="0" stop-color="#f4f6f9"/>
        <stop offset="0.6" stop-color="#e3ebf3"/>
        <stop offset="1" stop-color="#d9c2b2"/>
      </linearGradient>
      <linearGradient id="fade-white" x1="0" y1="0" x2="0" y2="1">
        <stop offset="0" stop-color="#ffffff" stop-opacity="0"/>
        <stop offset="1" stop-color="#ffffff" stop-opacity="1"/>
      </linearGradient>
      <radialGradient id="ring-orange" cx="0.5" cy="0.5" r="0.5">
        <stop offset="0.8" stop-color="#f5895a"/>
        <stop offset="1" stop-color="#e65a1d"/>
      </radialGradient>
      <radialGradient id="ring-dark" cx="0.5" cy="0.5" r="0.5">
        <stop offset="0.8" stop-color="#333333"/>
        <stop offset="1" stop-color="#1a1a1a"/>
      </radialGradient>

      <g id="brand-header">
        <rect x="0" y="0" width="314" height="6" fill="var(--black)"/>
        <rect x="314" y="0" width="314" height="6" fill="var(--orange)"/>
        <circle cx="70" cy="72" r="30" fill="var(--orange)"/>
        <text class="brand-name" x="118" y="90">BRIGHTDESK</text>
      </g>

      <g id="contact-footer">
        <circle cx="49" cy="1465" r="19" fill="var(--orange)"/>
        <g stroke="var(--white)" stroke-width="1.6" fill="none">
          <circle cx="49" cy="1465" r="9"/>
          <ellipse cx="49" cy="1465" rx="4" ry="9"/>
          <line x1="40" y1="1465" x2="58" y2="1465"/>
        </g>
        <text class="contact-line" x="82" y="1470">www.brightdeskit.com.au</text>
        <circle cx="49" cy="1510" r="19" fill="var(--orange)"/>
        <g stroke="var(--white)" stroke-width="1.6" fill="none">
          <rect x="40" y="1504" width="18" height="12"/>
          <polyline points="40,1504 49,1511 58,1504"/>
        </g>
        <text class="contact-line" x="82" y="1515">support@brightdeskit.com.au</text>
        <line x1="341" y1="1450" x2="341" y2="1530" stroke="var(--black)" stroke-width="2"/>
        <path d="M362,1478 q-6,4 -2,14 q6,14 20,20 q10,4 14,-2 l-7,-7 q-3,3 -7,1 q-8,-5 -12,-12 q-2,-4 1,-7 z" fill="var(--orange)"/>
        <path d="M383,1476 a10,10 0 0 1 10,10 M383,1470 a16,16 0 0 1 16,16" stroke="var(--orange)" stroke-width="2" fill="none"/>
        <text class="phone-number" x="405" y="1500">1300 555 014</text>
        <rect x="0" y="1564" width="314" height="6" fill="var(--black)"/>
        <rect x="314" y="1564" width="314" height="6" fill="var(--orange)"/>
      </g>

      <g id="top-swoosh">
        <path d="M0,150 Q314,95 628,175 L628,200 Q314,118 0,162 Z" fill="#9e9e9e"/>
        <path d="M240,128 Q460,120 628,190 L628,280 Q470,150 240,128 Z" fill="var(--black)"/>
        <path d="M0,166 Q314,124 628,260 L628,272 Q314,138 0,176 Z" fill="var(--orange)"/>
      </g>
    </defs>
  </svg>

  <section class="banner banner--front" aria-label="Front banner: cloud phone system and internet">
    <svg viewBox="0 0 628 1570">
      <rect width="628" height="1570" fill="url(#panel-bg)"/>
      <use href="#brand-header"/>

      <rect x="0" y="560" width="628" height="440" fill="url(#dark-section)"/>
      <path d="M0,690 C80,770 200,815 314,815 C450,815 560,770 628,705 L628,740 C560,800 450,840 314,840 C190,840 80,800 0,730 Z" fill="var(--orange-deep)"/>
      <path d="M0,660 C60,740 180,800 314,800 C450,800 560,760 628,700 L628,730 C560,790 450,822 314,822 C180,822 60,770 0,700 Z" fill="var(--orange)"/>
      <path d="M0,170 Q314,128 628,268 L628,640 C560,730 440,775 314,775 C180,775 60,730 0,665 Z" fill="var(--white)"/>
      <path d="M240,752 C420,760 560,700 628,620 L628,650 C560,730 430,770 240,752 Z" fill="var(--orange-soft)"/>

      <g role="img" aria-label="Photo of a smiling support agent wearing a headset, with colleagues blurred behind her">
        <path d="M6,175 Q314,132 628,272 L628,540 L6,540 Z" fill="url(#photo-tones)"/>
        <rect x="6" y="430" width="622" height="120" fill="url(#fade-white)"/>
      </g>

      <use href="#top-swoosh"/>

      <text class="headline" x="314" y="608" font-size="62">CLOUD PHONE</text>
      <text class="headline" x="314" y="658" font-size="40">SYSTEM &amp; INTERNET</text>
      <rect x="248" y="678" width="67" height="4" fill="var(--black)"/>
      <rect x="315" y="678" width="67" height="4" fill="var(--orange)"/>

      <text x="314" y="866" text-anchor="middle" font-size="37"><tspan class="lead-light">MELBOURNE’S </tspan><tspan class="lead-bold">LEADING</tspan></text>
      <text class="lead-white" x="314" y="916">IT SUPPORT</text>

      <path d="M0,992 L628,992 L628,1355 Q314,1485 0,1355 Z" fill="var(--orange)"/>
      <path d="M0,1345 Q314,1475 628,1345 L628,1355 Q314,1485 0,1355 Z" fill="var(--orange-deep)"/>

      <rect x="123" y="955" width="383" height="73" rx="36" fill="url(#silver-pill)" stroke="#ffffff" stroke-width="2"/>
      <text class="pill-text" x="314" y="1004"><tspan class="pill-light">OUR </tspan><tspan class="pill-bold">SOLUTIONS</tspan></text>

      <g stroke="var(--white)" stroke-width="2">
        <line x1="171" y1="1075" x2="171" y2="1260"/>
        <line x1="316" y1="1075" x2="316" y2="1260"/>
        <line x1="458" y1="1075" x2="458" y2="1260"/>
      </g>

      <g transform="translate(100,1133)">
        <circle r="58" fill="url(#ring-orange)"/>
        <circle r="48" fill="var(--white)"/>
        <circle cx="0" cy="-8" r="10" fill="var(--orange)"/>
        <path d="M-14,-8 a14,14 0 0 1 28,0" stroke="var(--orange)" stroke-width="3" fill="none"/>
        <path d="M-20,22 Q-20,6 0,6 Q20,6 20,22 Z" fill="var(--orange)"/>
        <path d="M0,8 l-3,6 l3,6 l3,-6 z" fill="var(--white)"/>
      </g>
      <g transform="translate(242,1133)">
        <circle r="58" fill="url(#ring-orange)"/>
        <circle r="48" fill="var(--white)"/>
        <rect x="-22" y="-20" width="30" height="22" rx="4" fill="none" stroke="var(--orange)" stroke-width="3"/>
        <circle cx="-12" cy="-9" r="2" fill="var(--orange)"/><circle cx="-3" cy="-9" r="2" fill="var(--orange)"/>
        <path d="M-4,6 h22 a4,4 0 0 0 4,-4 v-10 h-10 v10 a4,4 0 0 1 -4,4 z M4,6 l-4,10 l10,-10" fill="var(--orange)"/>
      </g>
      <g transform="translate(386,1133)">
        <circle r="58" fill="url(#ring-orange)"/>
        <circle r="48" fill="var(--white)"/>
        <rect x="-24" y="-22" width="48" height="30" rx="2" fill="none" stroke="var(--orange)" stroke-width="3"/>
        <path d="M6,-18 l8,5 l-8,5 z" fill="var(--orange)"/>
        <circle cx="-10" cy="-8" r="5" fill="var(--orange)"/>
        <path d="M-18,8 Q-10,-2 -2,8 Z" fill="var(--orange)"/>
        <circle cx="-14" cy="14" r="4" fill="var(--orange)"/><circle cx="0" cy="14" r="4" fill="var(--orange)"/><circle cx="14" cy="14" r="4" fill="var(--orange)"/>
        <rect x="-24" y="19" width="48" height="5" fill="var(--orange)"/>
      </g>
      <g transform="translate(528,1133)">
        <circle r="58" fill="url(#ring-orange)"/>
        <circle r="48" fill="var(--white)"/>
        <g stroke="var(--orange)" stroke-width="5" fill="none" stroke-linecap="round">
          <path d="M-24,-6 a34,34 0 0 1 48,0"/>
          <path d="M-15,3 a21,21 0 0 1 30,0"/>
          <path d="M-7,11 a10,10 0 0 1 14,0"/>
        </g>
        <circle cx="0" cy="19" r="4" fill="var(--orange)"/>
      </g>

      <text class="service-label" x="100" y="1218">VoIP &amp; Phone</text>
      <text class="service-label" x="100" y="1238">Systems</text>
      <text class="service-label" x="242" y="1218">SMS</text>
      <text class="service-label" x="242" y="1238">Gateway</text>
      <text class="service-label" x="386" y="1218">Cloud Team</text>
      <text class="service-label" x="386" y="1238">Calling</text>
      <text class="service-label" x="528" y="1218">5G, Fibre &amp;</text>
      <text class="service-label" x="528" y="1238">4G Internet</text>

      <rect x="128" y="1282" width="372" height="53" rx="26.5" fill="var(--black)"/>
      <text class="cta-text" x="314" y="1320">TALK TO US TODAY</text>
      <text class="cta-sub" x="314" y="1360">for <tspan class="cta-sub-bold">IT support</tspan> and <tspan class="cta-sub-bold">more!</tspan>...</text>
      <line x1="105" y1="1381" x2="190" y2="1381" stroke="var(--orange-soft)" stroke-width="1"/>
      <line x1="440" y1="1381" x2="523" y2="1381" stroke="var(--orange-soft)" stroke-width="1"/>
      <text class="web-caps" x="314" y="1387">WWW.BRIGHTDESKIT.COM.AU</text>

      <use href="#contact-footer"/>
    </svg>
  </section>

  <section class="banner banner--back" aria-label="Back banner: managed IT services">
    <svg viewBox="0 0 628 1570">
      <rect width="628" height="1570" fill="url(#panel-bg)"/>
      <use href="#brand-header"/>

      <path d="M0,1355 Q314,1490 628,1355 L628,1375 Q314,1510 0,1375 Z" fill="#4a4a4a"/>
      <path d="M0,560 L628,560 L628,1355 Q314,1485 0,1355 Z" fill="url(#dark-section)"/>
      <path d="M0,690 C80,770 200,815 314,815 C450,815 560,770 628,705 L628,740 C560,800 450,840 314,840 C190,840 80,800 0,730 Z" fill="var(--orange-deep)"/>
      <path d="M0,660 C60,740 180,800 314,800 C450,800 560,760 628,700 L628,730 C560,790 450,822 314,822 C180,822 60,770 0,700 Z" fill="var(--orange)"/>
      <path d="M0,170 Q314,128 628,268 L628,640 C560,730 440,775 314,775 C180,775 60,730 0,665 Z" fill="var(--white)"/>
      <path d="M240,752 C420,760 560,700 628,620 L628,650 C560,730 430,770 240,752 Z" fill="var(--orange-soft)"/>

      <g role="img" aria-label="Sketched cloud network linking computers, servers, tablets and laptops, held above an open hand">
        <path d="M30,195 Q314,150 628,285 L628,580 L30,560 Z" fill="url(#sketch-tones)" opacity="0.85"/>
        <rect x="30" y="480" width="598" height="100" fill="url(#fade-white)"/>
      </g>

      <use href="#top-swoosh"/>

      <text class="headline" x="314" y="626" font-size="62">MANAGED I.T</text>
      <text class="headline" x="314" y="683" font-size="40">SERVICES</text>
      <rect x="248" y="698" width="67" height="4" fill="var(--black)"/>
      <rect x="315" y="698" width="67" height="4" fill="var(--orange)"/>

      <rect x="123" y="830" width="383" height="73" rx="36" fill="url(#silver-pill)" stroke="#ffffff" stroke-width="2"/>
      <text class="pill-text" x="314" y="879"><tspan class="pill-light">OUR </tspan><tspan class="pill-bold">SOLUTIONS</tspan></text>

      <g stroke="var(--white)" stroke-width="2">
        <line x1="228" y1="945" x2="228" y2="1125"/>
        <line x1="400" y1="945" x2="400" y2="1125"/>
      </g>

      <g transform="translate(142,1000)">
        <circle r="62" fill="url(#ring-dark)"/>
        <circle r="50" fill="var(--white)"/>
        <circle cx="0" cy="-8" r="11" fill="var(--orange)"/>
        <path d="M-15,-8 a15,15 0 0 1 30,0" stroke="var(--orange)" stroke-width="3" fill="none"/>
        <path d="M-22,24 Q-22,7 0,7 Q22,7 22,24 Z" fill="var(--orange)"/>
        <path d="M0,9 l-3,7 l3,7 l3,-7 z" fill="var(--white)"/>
      </g>
      <g transform="translate(314,1000)">
        <circle r="62" fill="url(#ring-dark)"/>
        <circle r="50" fill="var(--white)"/>
        <path d="M0,-20 L16,-13 V2 Q16,16 0,22 Q-16,16 -16,2 V-13 Z" fill="var(--orange)"/>
        <rect x="-6" y="-2" width="12" height="10" fill="var(--white)"/>
        <path d="M-4,-2 v-4 a4,4 0 0 1 8,0 v4" stroke="var(--white)" stroke-width="2" fill="none"/>
        <g stroke="var(--orange)" stroke-width="2">
          <line x1="-32" y1="-8" x2="-20" y2="-8"/><line x1="20" y1="-8" x2="32" y2="-8"/>
          <line x1="-32" y1="8" x2="-20" y2="8"/><line x1="20" y1="8" x2="32" y2="8"/>
        </g>
      </g>
      <g transform="translate(487,1000)">
        <circle r="62" fill="url(#ring-dark)"/>
        <circle r="50" fill="var(--white)"/>
        <path d="M-22,14 a10,10 0 0 1 0,-20 a14,14 0 0 1 26,-6 a12,12 0 0 1 18,14 a6,6 0 0 1 0,12 z" fill="var(--orange)"/>
        <path d="M0,-8 l-8,9 h5 v8 h6 v-8 h5 z" fill="var(--white)"/>
      </g>
      <g transform="translate(228,1215)">
        <circle r="62" fill="url(#ring-dark)"/>
        <circle r="50" fill="var(--white)"/>
        <rect x="-22" y="-15" width="44" height="30" rx="2" fill="var(--orange)"/>
        <polyline points="-22,-15 0,3 22,-15" stroke="var(--white)" stroke-width="3" fill="none"/>
      </g>
      <g transform="translate(401,1215)">
        <circle r="62" fill="url(#ring-dark)"/>
        <circle r="50" fill="var(--white)"/>
        <rect x="-10" y="-24" width="34" height="28" rx="2" fill="none" stroke="var(--orange)" stroke-width="3"/>
        <line x1="-10" y1="-16" x2="24" y2="-16" stroke="var(--orange)" stroke-width="3"/>
        <g stroke="var(--orange)" stroke-width="2.5" fill="var(--white)">
          <circle cx="-8" cy="8" r="16"/>
          <ellipse cx="-8" cy="8" rx="7" ry="16" fill="none"/>
          <line x1="-24" y1="8" x2="8" y2="8"/>
        </g>
      </g>

      <text class="service-label" x="142" y="1080">Managed I.T</text>
      <text class="service-label" x="142" y="1100">Support</text>
      <text class="service-label" x="314" y="1080">Cybersecurity</text>
      <text class="service-label" x="314" y="1100">Solutions</text>
      <text class="service-label" x="487" y="1080">Cloud Servers &amp;</text>
      <text class="service-label" x="487" y="1100">Backups</text>
      <text class="service-label" x="228" y="1296">Office Suite</text>
      <text class="service-label" x="228" y="1316">Email Packs</text>
      <text class="service-label" x="401" y="1296">Domains &amp;</text>
      <text class="service-label" x="401" y="1316">Websites</text>

      <line x1="60" y1="1363" x2="100" y2="1363" stroke="#8a8a8a" stroke-width="1"/>
      <line x1="528" y1="1363" x2="568" y2="1363" stroke="#8a8a8a" stroke-width="1"/>
      <text class="web-caps web-caps--orange" x="314" y="1370">WWW.BRIGHTDESKIT.COM.AU</text>

      <use href="#contact-footer"/>
    </svg>
  </section>

  <p class="side-label side-label--front">FRONT</p>
  <p class="side-label side-label--back">BACK</p>
</main>
</body>
</html>
```